Calloway Teaching Placements Business Cards

We need business cards designed for our growing recruitment business.
We have just launched our offices in Sydney Melbourne and have a well established business in Perth. We are a fun young firm that specialise in Early Years Education Recruitment.
Our vision mission values are below
Our Vision:
To be:
the single, nationally recognised leader in the Early Childhood Sector.
a multifaceted organisation with a network of expertly driven facilities in the Early Childhood Sector, acknowledged as an organisation of integrity, innovation, heart and community.

Our Mission:
To provide superior quality recruitment services and solutions to the Early Childhood sector.
We empower our candidates to succeed.
We engage in trusted partnerships with our clients.
We grow our business/network/community, with passion and integrity.

Our Values:

We… are REAL
think: CUSTOMER
find: SOLUTIONS
achieve: RESULTS
enjoy: WHAT WE DO

Our website is www.callowayteaching.com feel free to visit it for inspiration.
Name Felix Harrowby
Title National Director
1300 047 815
0412 736 205
felix@callowayplacements.com
website www.callowayteaching.com

I have attached our current business cards and logo designs to view

Target Market(s)

Recruitment

Industry/Entity Type

Business

Contact Information for Business Card

Name Felix Harrowby
Title National Director
1300 047 815
0412 736 205

Font styles to use
Serif

Requirements
Must have
• Company Values and the cities we have offices in Perth | Sydney | Melbourne
Nice to have
• Our Vision on the card
• Our Vision:
• To be a nationally recognised leader in the Early Childhood Sector.
• A multifaceted organisation with a network of expertly driven facilities in the Early Childhood Sector, acknowledged as an organisation of integrity, innovation, heart and community.

```html
<!DOCTYPE html>
<html lang="en">
<head>
<meta charset="utf-8">
<title>Calloway Teaching Placements – Business Cards</title>
<link rel="stylesheet" href="https://fonts.googleapis.com/css2?family=Source+Sans+3:wght@400;600&display=swap">
<style>
  :root {
    --bg: #e9e6e1;
    --blue-light: #2a9ad6;
    --blue-mid: #1b78b8;
    --blue-deep: #0c5a92;
    --blue-accent: #2aa8e0;
    --name-blue: #1d76b6;
    --ink: #333a40;
    --white: #ffffff;
    --card-shadow: 0 10px 28px rgba(0, 0, 0, 0.18);
  }
  * { box-sizing: border-box; margin: 0; padding: 0; }
  html, body {
    width: 1200px; height: 900px; overflow: hidden;
    background: var(--bg);
    font-family: "Source Sans 3", "Myriad Pro", Arial, sans-serif;
  }
  .sheet {
    width: 1200px; height: 900px;
    display: flex; flex-direction: column; align-items: center; justify-content: center;
    gap: 50px;
  }
  .card {
    position: relative; width: 640px; height: 366px;
    box-shadow: var(--card-shadow); overflow: hidden;
  }

  /* Front */
  .card--front {
    background: linear-gradient(180deg, var(--blue-light) 0%, var(--blue-mid) 55%, var(--blue-deep) 100%);
    color: var(--white);
  }
  .brand {
    position: absolute; left: 130px; top: 86px;
    display: flex; align-items: center; gap: 20px;
  }
  .brand__circle {
    width: 104px; height: 104px; border-radius: 50%;
    border: 3px solid var(--white); flex: none;
  }
  .brand__name {
    font-weight: 400; font-size: 25px; letter-spacing: 1.2px; text-transform: uppercase;
  }
  .brand__tagline { font-size: 13.5px; font-weight: 400; margin-top: 4px; letter-spacing: 0.2px; }
  .front__cities {
    position: absolute; left: 0; right: 0; top: 214px; text-align: center; font-size: 16px; letter-spacing: 0.3px;
  }
  .front__social {
    position: absolute; left: 0; right: 0; top: 252px; display: flex; justify-content: center; align-items: center; gap: 8px;
    font-size: 16px;
  }
  .front__social-label { margin-right: 8px; }
  .front__social-dot { width: 15px; height: 15px; background: var(--white); border-radius: 3px; }
  .front__values {
    position: absolute; left: 0; right: 0; top: 306px; text-align: center;
    font-size: 12.5px; letter-spacing: 0.6px; opacity: 0.9;
  }

  /* Back */
  .card--back { background: var(--white); color: var(--ink); }
  .back__wave { position: absolute; inset: 0; }
  .person { position: absolute; left: 46px; top: 74px; }
  .person__name { color: var(--name-blue); font-weight: 600; font-size: 27px; line-height: 1; }
  .person__title { font-size: 17px; margin-top: 4px; margin-left: 8px; }
  .back__brand {
    position: absolute; right: 34px; top: 26px; display: flex; align-items: center; gap: 12px;
  }
  .back__brand-name { color: var(--name-blue); font-size: 15px; font-weight: 400; letter-spacing: 0.8px; text-transform: uppercase; }
  .back__brand-circle {
    width: 130px; height: 130px; border-radius: 50%; border: 4px solid var(--blue-mid);
  }
  .contacts { position: absolute; left: 56px; top: 222px; list-style: none; font-size: 17px; line-height: 23px; }
  .contacts li { display: flex; align-items: center; gap: 10px; }
  .contacts svg { width: 13px; height: 13px; fill: var(--blue-deep); flex: none; }
  .back__web {
    position: absolute; right: 22px; top: 280px; color: var(--white); font-size: 15px; letter-spacing: 0.2px;
  }
</style>
</head>
<body>
<main class="sheet">

  <section class="card card--front" aria-label="Card front">
    <div class="brand">
      <span class="brand__circle"></span>
      <div>
        <div class="brand__name">Calloway Teaching</div>
        <div class="brand__tagline">Bringing quality to education recruitment</div>
      </div>
    </div>
    <p class="front__cities">Perth | Sydney | Melbourne</p>
    <div class="front__social">
      <span class="front__social-label">Find us on:</span>
      <span class="front__social-dot"></span>
      <span class="front__social-dot"></span>
      <span class="front__social-dot"></span>
      <span class="front__social-dot"></span>
    </div>
    <p class="front__values">We are REAL · think CUSTOMER · find SOLUTIONS · achieve RESULTS · enjoy WHAT WE DO</p>
  </section>

  <section class="card card--back" aria-label="Card back">
    <svg class="back__wave" viewBox="0 0 640 366" preserveAspectRatio="none" aria-hidden="true">
      <defs>
        <linearGradient id="waveFill" x1="0" y1="0" x2="1" y2="1">
          <stop offset="0" stop-color="#1b78b8"/>
          <stop offset="1" stop-color="#0c5a92"/>
        </linearGradient>
      </defs>
      <path d="M0,318 C190,372 420,318 640,168 L640,366 L0,366 Z" fill="#2aa8e0"/>
      <path d="M0,342 C230,366 440,300 640,150 L640,366 L0,366 Z" fill="url(#waveFill)"/>
      <path d="M0,330 C200,372 420,320 600,190 C430,330 210,352 0,338 Z" fill="#2aa8e0"/>
    </svg>

    <div class="person">
      <h1 class="person__name">Felix Harrowby</h1>
      <p class="person__title">National Director</p>
    </div>

    <div class="back__brand">
      <span class="back__brand-name">Calloway Teaching</span>
      <span class="back__brand-circle"></span>
    </div>

    <ul class="contacts">
      <li>
        <svg viewBox="0 0 16 16"><path d="M2 6c0-2 2-3 6-3s6 1 6 3v1h-3V6H5v1H2z M4 8h8l1 5H3z"/></svg>
        1300 047 815
      </li>
      <li>
        <svg viewBox="0 0 16 16"><path d="M4 1h8v14H4z M5.5 2.5v9h5v-9z M7 12.5h2v1H7z" fill-rule="evenodd"/></svg>
        0412 736 205
      </li>
      <li>
        <svg viewBox="0 0 16 16"><path d="M1 3h14v10H1z M2 4l6 5 6-5v-0.2H2z" fill-rule="evenodd"/></svg>
        felix@callowayplacements.com
      </li>
    </ul>

    <p class="back__web">www.callowayteaching.com</p>
  </section>

</main>
</body>
</html>
```